New Business Card Design Project

I need a meaningful new business card. Therefore, the website should convey growth, joy, uniqueness, workout and a bit of luxury.
Color scheme should be petrol, gold and matching colors.

```html
<!DOCTYPE html>
<html lang="de">
<head>
<meta charset="utf-8">
<title>Business Card – Mira Lindqvist</title>
<link href="https://fonts.googleapis.com/css2?family=Great+Vibes&family=Marcellus+SC&family=Montserrat:wght@400&display=swap" rel="stylesheet">
<style>
  :root {
    --stage: #9b9b9b;
    --card-light: #ffffff;
    --petrol-deep: #0d1e21;
    --petrol-dark: #0a1517;
    --petrol: #15505a;
    --gold: #c9a04a;
    --gold-light: #e2c27a;
    --gold-deep: #a9802f;
    --text-soft: #3a3a3a;
    --ornament: #ececec;
  }
  * { margin: 0; padding: 0; box-sizing: border-box; }
  html, body { width: 1200px; height: 1200px; overflow: hidden; }
  body { background: var(--stage); position: relative; }

  .card {
    position: absolute;
    left: 226px;
    width: 746px;
    height: 436px;
    border-radius: 28px;
    overflow: hidden;
  }
  .card--front { top: 139px; background: var(--card-light); }
  .card--back {
    top: 621px;
    background: radial-gradient(ellipse at 50% 45%, var(--petrol-deep) 0%, var(--petrol-dark) 75%);
  }

  .front__ornament {
    position: absolute;
    left: 415px;
    top: 40px;
    width: 331px;
    height: 372px;
    border-radius: 60% 0 0 55%;
    background: linear-gradient(200deg, #f1f1f1 0%, var(--ornament) 50%, #f6f6f6 100%);
  }

  .front__name {
    position: absolute;
    left: 56px;
    top: 184px;
    font-family: "Great Vibes", cursive;
    font-weight: 400;
    font-size: 62px;
    line-height: 1;
    color: var(--gold);
  }
  .front__role {
    position: absolute;
    left: 60px;
    top: 244px;
    font-family: "Marcellus SC", serif;
    font-size: 20px;
    letter-spacing: 2.4px;
    color: var(--petrol);
  }
  .contact-list {
    position: absolute;
    left: 60px;
    top: 299px;
    list-style: none;
    font-family: "Montserrat", sans-serif;
    font-size: 18px;
    color: var(--text-soft);
  }
  .contact-list__item {
    display: flex;
    align-items: center;
    height: 24px;
  }
  .contact-list__icon {
    width: 14px;
    height: 14px;
    margin-right: 17px;
    fill: var(--gold);
  }

  .back__mark {
    position: absolute;
    left: 293px;
    top: 84px;
    width: 160px;
    height: 160px;
    border-radius: 50%;
    border: 2px solid var(--gold);
  }
  .back__brand {
    position: absolute;
    left: 0;
    right: 0;
    top: 272px;
    text-align: center;
    font-family: "Marcellus SC", serif;
    font-size: 44px;
    letter-spacing: 3px;
    color: var(--gold);
  }
</style>
</head>
<body>

  <section class="card card--front">
    <div class="front__ornament" role="img" aria-label="Faint grey floral vine ornament with leaves"></div>
    <h1 class="front__name">Mira Lindqvist</h1>
    <p class="front__role">Pilates Studio Trainerin</p>
    <ul class="contact-list">
      <li class="contact-list__item">
        <svg class="contact-list__icon" viewBox="0 0 24 24" aria-hidden="true"><path d="M6.6 10.8a15.1 15.1 0 0 0 6.6 6.6l2.2-2.2c.3-.3.7-.4 1-.2 1.1.4 2.3.6 3.6.6.6 0 1 .4 1 1V20c0 .6-.4 1-1 1C10.6 21 3 13.4 3 4c0-.6.4-1 1-1h3.5c.6 0 1 .4 1 1 0 1.3.2 2.5.6 3.6.1.3 0 .7-.2 1z"/></svg>
        +49 170 5550128
      </li>
      <li class="contact-list__item">
        <svg class="contact-list__icon" viewBox="0 0 24 24" aria-hidden="true"><path d="M2 6.5 12 13l10-6.5V19H2z"/><path d="M2 5h20l-10 6.5z"/></svg>
        info@pilates-seewinkel.de
      </li>
      <li class="contact-list__item">
        <svg class="contact-list__icon" viewBox="0 0 24 24" aria-hidden="true"><circle cx="12" cy="12" r="9" fill="none" stroke="var(--gold)" stroke-width="2"/><path d="M3 12h18M12 3c3 3.5 3 14.5 0 18M12 3c-3 3.5-3 14.5 0 18" fill="none" stroke="var(--gold)" stroke-width="1.6"/></svg>
        pilates-seewinkel.de
      </li>
    </ul>
  </section>

  <section class="card card--back">
    <div class="back__mark" aria-hidden="true"></div>
    <p class="back__brand">Kernform Studio</p>
  </section>

</body>
</html>
```